Business Card Design - Construction Company

Tarrowin Construction is in need of a sharp, modern business card design that has an architectural/high fashion feel.

We are looking for a two sided card.

One side simple dark grey/black with some texture in the background. e.g. (a mosaic of simple interconnecting shapes or a shadow of the logo.) Something to draw attention and create interest.It will need to feature a large Tarrowin construction logo (files attached) in metallic gradient or plain white.

The other side should contain all of our information:

(in largest text)
Name of person
Tarrowin Construction Pty. Ltd.

Licensed builders specialising in:
- Bathrooms
- Kitchens
- Commercial interiors

(mid sized text)
Phone number
Fax number
person@tarrowinconstruction.example.au
www. tarrowinconstruction.example.au

(smaller text)
ABN: 62407938215
BSA license: xxx-xxxx
PO Box 8641 Kellsmoor QLD 4019 (address)

Target Market(s)

professional home and business owners

Industry/Entity Type

Construction

Requirements
Must have
• Must be bold, professional looking and modern.
Nice to have
• We are undecided as to what kind of printing we will go with.
Definitely square edged.
Probably high quality satin card.
We are also interested in designs that would work well on transparent or translucent plastic.
Ideally we would print two versions.
Should not have
• Nothing with an antique feel.
No wild colours. Small amounts of colour can be good in the right place.

```html
<!DOCTYPE html>
<html lang="en">
<head>
<meta charset="utf-8">
<title>Tarrowin Construction – Business Cards</title>
<link rel="stylesheet" href="https://fonts.googleapis.com/css2?family=Michroma&family=Questrial&display=swap">
<style>
  :root {
    --backdrop: #3b3b3d;
    --ink: #2e2e30;
    --ink-soft: #3c3c3e;
    --band: #5b5b5d;
    --band-text: #f2f2f2;
    --info-bg: #d5d5d7;
    --info-bg-light: #dcdcde;
    --sky: #cfe6f3;
    --sand: #b9a68c;
  }
  * { box-sizing: border-box; margin: 0; padding: 0; }
  html, body {
    width: 1200px; height: 1080px; overflow: hidden;
    background: var(--backdrop);
  }
  .card {
    position: absolute; top: 122px;
    width: 480px; height: 838px;
    overflow: hidden;
    box-shadow: 0 6px 18px rgba(0,0,0,.45);
  }
  .card--tiles { left: 79px; }
  .card--glass { left: 641px; }

  .hero {
    position: absolute; left: 0; top: 0; width: 480px; height: 482px;
  }
  .card--tiles .hero {
    background: linear-gradient(180deg, #d7ebf6 0%, #c9dbe4 14%, #bfb3a0 40%, var(--sand) 58%, #c7c9c6 78%, #dff1fb 100%);
  }
  .card--glass .hero {
    background: linear-gradient(180deg, #e6f4fc 0%, #c5e0ef 16%, #c2b6a2 40%, var(--sand) 58%, #cfd6d6 80%, #e3f3fb 100%);
  }
  .wordmark {
    position: absolute; left: 0; right: 0; top: 318px;
    text-align: center;
    font-family: "Michroma", sans-serif;
    color: var(--ink);
    font-size: 33px; line-height: 52px; letter-spacing: 1px;
    text-transform: uppercase;
  }

  .band {
    position: absolute; left: 0; top: 482px; width: 480px; height: 84px;
    background: var(--band);
    color: var(--band-text);
    text-align: center;
    font-family: "Michroma", sans-serif;
    text-transform: uppercase;
  }
  .band__title { position: absolute; left: 0; right: 0; top: 20px; font-size: 16px; letter-spacing: .5px; }
  .band__list { position: absolute; left: 0; right: 0; top: 47px; font-size: 11.5px; letter-spacing: .3px; }

  .info {
    position: absolute; left: 0; top: 566px; width: 480px; height: 272px;
    font-family: "Questrial", sans-serif;
    color: var(--ink);
    font-variant: small-caps;
    text-align: center;
  }
  .card--tiles .info { background: var(--info-bg); }
  .card--glass .info { background: linear-gradient(160deg, #e4e4e6 0%, var(--info-bg-light) 50%, #cfcfd1 100%); }

  .line { position: absolute; left: 0; right: 0; white-space: nowrap; }
  .name { top: 26px; font-size: 27px; font-weight: 700; font-family: "Michroma", sans-serif; font-variant: normal; font-size: 22px; letter-spacing: .5px; }
  .company { top: 56px; font-size: 18px; color: var(--ink-soft); letter-spacing: .6px; }
  .address { top: 84px; font-size: 18px; letter-spacing: .6px; }
  .contact { font-size: 17px; letter-spacing: .5px; display: flex; justify-content: center; align-items: center; gap: 8px; }
  .phone { top: 114px; }
  .fax { top: 132px; }
  .email { top: 151px; }
  .web { top: 169px; }
  .abn { top: 199px; font-size: 15px; letter-spacing: .6px; }
  .bsa { top: 219px; font-size: 15px; letter-spacing: .6px; }
  .icon { width: 14px; height: 14px; flex: none; fill: var(--ink); }
</style>
</head>
<body>

<svg width="0" height="0" style="position:absolute" aria-hidden="true">
  <symbol id="i-phone" viewBox="0 0 16 16"><path d="M2 6c0-2 2.5-3 6-3s6 1 6 3v1.5h-3.5V6H5.5v1.5H2z"/><path d="M4 8.5h8l1.5 5h-11z"/></symbol>
  <symbol id="i-fax" viewBox="0 0 16 16"><path d="M3 4h10v3H3z"/><path d="M1.5 8h13v6h-13z"/><rect x="5" y="1.5" width="6" height="2"/></symbol>
  <symbol id="i-mail" viewBox="0 0 16 16"><path d="M1 3.5h14v9H1z" fill="none" stroke="currentColor" stroke-width="1.4"/><path d="M1 3.5 8 9l7-5.5" fill="none" stroke="currentColor" stroke-width="1.4"/></symbol>
  <symbol id="i-web" viewBox="0 0 16 16"><circle cx="8" cy="8" r="6.5" fill="none" stroke="currentColor" stroke-width="1.3"/><ellipse cx="8" cy="8" rx="2.8" ry="6.5" fill="none" stroke="currentColor" stroke-width="1.1"/><path d="M1.5 8h13M2.5 5h11M2.5 11h11" stroke="currentColor" stroke-width="1"/></symbol>
</svg>

<!-- Version with tiled glass backdrop -->
<section class="card card--tiles">
  <div class="hero" role="img" aria-label="Soft blue and sand frosted glass backdrop with overlapping translucent tiles"></div>
  <div class="wordmark">Tarrowin<br>Construction</div>
  <div class="band">
    <div class="band__title">Licensed builders specialising in:</div>
    <div class="band__list">Bathrooms | Kitchens | Commercial interiors</div>
  </div>
  <div class="info">
    <div class="line name">Lukas Varden</div>
    <div class="line company">Tarrowin Construction Pty. Ltd.</div>
    <div class="line address">PO Box 8641 Kellsmoor QLD 4019</div>
    <div class="line contact phone"><svg class="icon"><use href="#i-phone"/></svg>000 000 0000</div>
    <div class="line contact fax"><svg class="icon"><use href="#i-fax"/></svg>000 000 0000</div>
    <div class="line contact email" style="color:var(--ink)"><svg class="icon"><use href="#i-mail"/></svg>person@tarrowinconstruction.example.au</div>
    <div class="line contact web" style="color:var(--ink)"><svg class="icon"><use href="#i-web"/></svg>www.tarrowinconstruction.example.au</div>
    <div class="line abn">ABN: 62407938215</div>
    <div class="line bsa">BSA license: xxx-xxxx</div>
  </div>
</section>

<!-- Version with rippled glass backdrop -->
<section class="card card--glass">
  <div class="hero" role="img" aria-label="Soft blue and sand rippled frosted glass backdrop"></div>
  <div class="wordmark">Tarrowin<br>Construction</div>
  <div class="band">
    <div class="band__title">Licensed builders specialising in:</div>
    <div class="band__list">Bathrooms | Kitchens | Commercial interiors</div>
  </div>
  <div class="info" role="img" aria-label="Pale grey panel with faint translucent tile texture">
    <div class="line name">Lukas Varden</div>
    <div class="line company">Tarrowin Construction Pty. Ltd.</div>
    <div class="line address">PO Box 8641 Kellsmoor QLD 4019</div>
    <div class="line contact phone"><svg class="icon"><use href="#i-phone"/></svg>000 000 0000</div>
    <div class="line contact fax"><svg class="icon"><use href="#i-fax"/></svg>000 000 0000</div>
    <div class="line contact email" style="color:var(--ink)"><svg class="icon"><use href="#i-mail"/></svg>person@tarrowinconstruction.example.au</div>
    <div class="line contact web" style="color:var(--ink)"><svg class="icon"><use href="#i-web"/></svg>www.tarrowinconstruction.example.au</div>
    <div class="line abn">ABN: 62407938215</div>
    <div class="line bsa">BSA license: xxx-xxxx</div>
  </div>
</section>

</body>
</html>
```